Velorine Jewellery Display Card

We are a jewellery manufacturer and need artwork for an A4 size strut card to advertise our new "Crescent Loop Pendant "
In the attached files is a picture of the new pendant and artwork for our trademark "Velorine"
We also need to include the phrase " an expression of love "
as part of the artwork.
The background colour should be predominately white

Target Market(s)

This product has been designed as a gift for Mothers as it has their children names
engraved on the pendant

Industry/Entity Type

Manufacturer

Font styles to use
Serif
Script

Colors
ffffff

Requirements
Must have
• Artwork should be simple and elegant , the predominant look in Australian jewellery stores which is where these display cards will be is white, bright and elegant

```html
<!DOCTYPE html>
<html lang="en">
<head>
<meta charset="utf-8">
<title>Velorine Display Card</title>
<link rel="stylesheet" href="https://fonts.googleapis.com/css2?family=Cinzel:wght@400&display=swap">
<style>
  :root {
    --backdrop: #000000;
    --card: #ffffff;
    --ink: #9a9a9a;
    --silver-light: #ececec;
    --silver-mid: #d6d6d6;
  }
  * { margin: 0; padding: 0; box-sizing: border-box; }
  html, body {
    width: 1153px;
    height: 1200px;
    overflow: hidden;
    background: var(--backdrop);
  }
  .strut-card {
    position: absolute;
    left: 231px;
    top: 132px;
    width: 691px;
    height: 936px;
    background: var(--card);
    border-radius: 34px;
  }
  .headline {
    position: absolute;
    left: 0;
    right: 0;
    top: 124px;
    text-align: center;
    font-family: "Cinzel", serif;
    font-weight: 400;
    font-size: 44px;
    line-height: 58px;
    letter-spacing: 3px;
    color: var(--ink);
  }
  .pendant-image {
    position: absolute;
    left: 225px;
    top: 364px;
    width: 236px;
    height: 320px;
    border-radius: 40% 40% 48% 48% / 34% 34% 52% 52%;
    background: radial-gradient(ellipse at 50% 58%, var(--silver-mid) 0%, var(--silver-light) 55%, var(--card) 100%);
  }
  .brand-name {
    position: absolute;
    left: 0;
    right: 0;
    top: 792px;
    text-align: center;
    font-family: "Cinzel", serif;
    font-weight: 400;
    font-size: 44px;
    line-height: 48px;
    letter-spacing: 1px;
    color: var(--ink);
  }
</style>
</head>
<body>
  <main class="strut-card">
    <h1 class="headline">AN<br>EXPRESSION<br>OF LOVE</h1>
    <div class="pendant-image" role="img" aria-label="Photograph of the silver Crescent Loop Pendant: nested rings engraved with children's names around a tree of life centre, hung from a stone-set bail"></div>
    <p class="brand-name">VELORINE</p>
  </main>
</body>
</html>
```